Design a business card & stationary for a mortgage company

We are looking for a good looking business card design for our mortgage company that includes our logo. We received a free design as part of our logo project but we don't love it. The company is called "Pinecrest Mortgage Company" so we like waves and lighthouses. The logo should be included. We have a version in both vertical and horizontal that we have provided.

Industry/Entity Type

Finance

Contact Information for Business Card

This should include our new logo file

Requirements
Must have
• 3. The details you'd like on the card - name, title, phone, email, website, address, social media handles etc.
1. Marcus Hale
Vice President
732-419-6253
Fax 888-304-2918
mhale@pinecrestmortgage.example
NMLS 47162 - Company NMLS 61290
18 Larkin Ave
Toms River, NJ 08614

```html
<!DOCTYPE html>
<html lang="en">
<head>
<meta charset="utf-8">
<title>Pinecrest Mortgage Company — Stationery</title>
<link rel="stylesheet" href="https://fonts.googleapis.com/css2?family=Lato:wght@400;700&family=Open+Sans:wght@400&display=swap">
<style>
  :root {
    --navy: #1d4a80;
    --sky: #2a8fd6;
    --ink: #3a3a3a;
    --ink-soft: #555;
    --paper: #ffffff;
    --backdrop: #e4e5e7;
  }
  * { box-sizing: border-box; margin: 0; padding: 0; }
  html, body { width: 1200px; height: 1200px; overflow: hidden; }
  body { background: var(--backdrop); position: relative; font-family: "Open Sans", sans-serif; color: var(--ink); }

  .sheet { position: absolute; background: var(--paper); box-shadow: 0 2px 6px rgba(0,0,0,.18); }

  /* Letterhead */
  .letterhead { left: 119px; top: 278px; width: 556px; height: 714px; }
  .brand { position: absolute; display: flex; align-items: center; gap: 8px; }
  .brand-dot { width: 12px; height: 12px; border-radius: 50%; background: var(--navy); flex: none; }
  .brand-name { font-family: "Lato", sans-serif; font-weight: 700; color: var(--navy); text-transform: uppercase; letter-spacing: .06em; line-height: 1.15; }
  .letterhead .brand { left: 0; right: 0; top: 34px; justify-content: center; }
  .letterhead .brand-name { font-size: 19px; text-align: left; }

  .letter { position: absolute; left: 52px; top: 128px; width: 452px; font-size: 8.6px; line-height: 11px; color: var(--ink-soft); }
  .letter .date { margin-bottom: 10px; }
  .letter .recipient { margin-bottom: 30px; }
  .letter .salutation { margin-bottom: 21px; }
  .letter .body p { line-height: 16px; margin-bottom: 16px; text-align: justify; }
  .letter .closing { margin-top: 24px; margin-bottom: 37px; }
  .signer-name { font-size: 11px; color: var(--ink); line-height: 14px; }
  .signer-title { margin-top: 4px; }

  .letter-footer { position: absolute; left: 0; right: 0; top: 664px; text-align: center; font-family: "Lato", sans-serif; color: var(--ink); }
  .footer-top { font-size: 10.4px; display: flex; justify-content: center; gap: 16px; }
  .footer-top .nmls { color: var(--sky); }
  .footer-rule { width: 454px; height: 2px; background: var(--navy); margin: 4px auto 5px; }
  .footer-contact { font-size: 9.4px; white-space: nowrap; }
  .footer-contact b { color: var(--navy); font-weight: 700; }
  .footer-contact .web { color: var(--sky); }

  /* Envelope front */
  .envelope-front { left: 715px; top: 492px; width: 432px; height: 216px; }
  .envelope-front .brand { left: 22px; top: 26px; }
  .envelope-front .brand-dot { width: 8px; height: 8px; }
  .envelope-front .brand-name { font-size: 11px; }
  .envelope-rule { position: absolute; left: 23px; right: 25px; top: 185px; height: 1px; background: var(--navy); }
  .envelope-address { position: absolute; left: 23px; top: 190px; font-family: "Lato", sans-serif; font-size: 7.6px; color: var(--ink); }

  /* Envelope back */
  .envelope-back { left: 717px; top: 743px; width: 429px; height: 213px; }
  .envelope-flap { position: absolute; left: 0; top: 0; width: 100%; height: 51px; background: var(--navy); clip-path: polygon(0 0, 100% 0, 96.5% 100%, 3.5% 100%); }
</style>
</head>
<body>

<section class="sheet letterhead" aria-label="Letterhead">
  <div class="brand">
    <span class="brand-dot"></span>
    <span class="brand-name">Pinecrest<br>Mortgage Company</span>
  </div>

  <div class="letter">
    <p class="date">Issuing Date: May 5, 2018</p>
    <p class="recipient">Name Of Employee Mr. XYZABC<br>Address of Employee<br>Address Line 2 etc..</p>
    <p class="salutation">Dear Mr.XYZABC</p>
    <div class="body">
      <p>Lorem Ipsum has been the industry's standard dummy text ever since the 1500s, when an unknown printer took a galley of type and scrambled it to make a type specimen book. It has survived not only five centuries, but also the leap into electronic typesetting, remaining essentially unchanged. It was popularised in the 1960s with the release of Transfer sheets containing Lorem Ipsum passages, and more recently with desktop publishing software like Folio Layout including versions of Lorem Ipsum.</p>
      <p>Lorem Ipsum is simply dummy text of the printing and typesetting industry. Lorem Ipsum has been the industry's standard dummy text ever since the 1500s, when an unknown printer took a galley of type and scrambled it to make a type specimen book.</p>
      <p>It has survived not only five centuries, but also the leap into electronic typesetting, remaining essentially unchanged. It was popularised in the 1960s with the release of Transfer sheets containing Lorem IpsumIpsum passages.</p>
    </div>
    <p class="closing">Yours Sincerely</p>
    <p class="signer-name">Daniel Ward</p>
    <p class="signer-title">Managing Director</p>
  </div>

  <footer class="letter-footer">
    <div class="footer-top">
      <span>18 Larkin Ave Toms River, NJ 08614</span>
      <span class="nmls">NMLS 47162 | Company NMLS 61290</span>
    </div>
    <div class="footer-rule"></div>
    <p class="footer-contact"><b>P:</b> 732-419-6253 | <b>F:</b> 888-304-2918 | <b>E:</b> mhale@pinecrestmortgage.example | <span class="web">www.pinecrestmortgage.example</span></p>
  </footer>
</section>

<section class="sheet envelope-front" aria-label="Envelope front">
  <div class="brand">
    <span class="brand-dot"></span>
    <span class="brand-name">Pinecrest<br>Mortgage Company</span>
  </div>
  <div class="envelope-rule"></div>
  <p class="envelope-address">18 Larkin Ave Toms River, NJ 08614</p>
</section>

<section class="sheet envelope-back" aria-label="Envelope back">
  <div class="envelope-flap"></div>
</section>

</body>
</html>
```